Flyer Design for a Boston Therapeutic Clinic

I am a body therapist who needs a couple of flyers designed:
1. To fit half a page.
2. To fit a 5 inch by 3.5 inch flyer.
My practice is based in Boston, MA and my web site is:
www.LarkfieldTane.Com
For the First half page:
A. Have my company's name and color shown as it appears on my web site (Larkfield Tane)
B. Have the following text: "Control your weight (This part should be emphasized) by balancing your nervous and digestive system through the Tane Method. The Tane Method, a technique developed by Dr. Wenna. Tane, uses physical pressure to manipulate visceral tissue to bring back resiliency and proper functioning of the whole body."
Also helps with
-Constipation
-Bloating
-IBS
-eating disorders and overeating
Our practitioner is highly experienced. Please visit our web sites for reviews.
C. I would like to have a nice earthy feeling, something that feels "freeing" like open flowers, or an open land scape such as mountains or fields.
D. I also like the color blue, white, orange; perhaps if these colors can be integrated into the flyer, that would be great.
E. "Visit our web site LarkfieldTane.com or call 413-908-2617"
The Smaller Flyer :
A.The smaller Flyer should also have my Company's name as shown on my web site (Larkfield Tane)
B.The following text: " Restore your body's natural resiliency and greatly reduce your physical pain through the Dr. Wenna Tane Method of Structural Integration."
C. "Our practitioner is highly experienced and has a great reputation; visit our web site for reviews."
"Benefits:
"reduce aches and pains
reduce joint pain
reduce chronic muscular tension"
D, "feel better after the first session!"
E. if you could use a picture of me working on someone from my web site, that would be great.
F. I also like the colors white, orange and silver, for this one.
G. "Visit our web site LarkfieldTane.com or call 413-908 2617"
I am very open minded,
I would like the flyer to evoke a sense of tranquility, professionalism, and simplicity. So if you have another angle you think would look good, then go for it! As long as it looks clean, professional and helpful.
Thanks a lot!
If you need any pictures from my web site, I have the original high resolution files that i can send.
Professionals and working men and women from ages 20-70
Clinic

```html
<!DOCTYPE html>
<html lang="en">
<head>
<meta charset="utf-8">
<title>Larkfield Tane Therapy – Pocket Folder</title>
<link href="https://fonts.googleapis.com/css2?family=Fira+Sans:wght@400;600&family=Cormorant+Garamond:wght@500&display=swap" rel="stylesheet">
<style>
  :root {
    --page: #ffffff;
    --flap: #e6e7e8;
    --navy: #2b3566;
    --band: #2f3d73;
    --white: #ffffff;
    --sky-top: #3f6fb8;
    --sky-mid: #9fbde0;
    --cloud: #e4ebf3;
    --field-light: #8cc66a;
    --field-dark: #1f7a3a;
    --strip-dark: #1d1b19;
    --bone: #b58a4e;
    --strip-grey: #b9bcb6;
    --name-grey: #5b5b5b;
  }
  html, body {
    margin: 0;
    padding: 0;
    width: 1200px;
    height: 916px;
    overflow: hidden;
    background: var(--page);
  }
  .canvas {
    position: relative;
    width: 1200px;
    height: 916px;
    font-family: "Fira Sans", Arial, sans-serif;
  }
  .pocket-flap {
    position: absolute;
    left: 0;
    top: 0;
  }
  .folder-face {
    position: absolute;
    left: 176px;
    top: 14px;
    width: 1010px;
    height: 696px;
  }
  .hero-photo {
    position: absolute;
    left: 0;
    top: 0;
    width: 1010px;
    height: 586px;
    background:
      radial-gradient(ellipse 45% 30% at 35% 18%, var(--cloud) 0%, rgba(228,235,243,0) 70%),
      radial-gradient(ellipse 30% 18% at 80% 55%, rgba(228,235,243,.8) 0%, rgba(228,235,243,0) 70%),
      linear-gradient(180deg, var(--sky-top) 0%, var(--sky-mid) 45%, var(--cloud) 62%, var(--field-light) 66%, var(--field-dark) 100%);
  }
  .divider-band {
    position: absolute;
    left: 0;
    top: 586px;
    width: 1010px;
    height: 9px;
    background: var(--band);
  }
  .anatomy-strip {
    position: absolute;
    left: 0;
    top: 595px;
    width: 505px;
    height: 101px;
    background:
      radial-gradient(ellipse 16% 70% at 17% 60%, var(--bone) 0%, rgba(181,138,78,0) 75%),
      radial-gradient(ellipse 16% 70% at 50% 60%, var(--bone) 0%, rgba(181,138,78,0) 75%),
      radial-gradient(ellipse 16% 70% at 83% 60%, var(--bone) 0%, rgba(181,138,78,0) 75%),
      var(--strip-dark);
  }
  .name-strip {
    position: absolute;
    left: 505px;
    top: 595px;
    width: 505px;
    height: 101px;
    background: linear-gradient(90deg, #aeb2ab 0%, var(--strip-grey) 50%, #c7c9c4 100%);
  }
  .brand-name {
    position: absolute;
    left: 43px;
    top: 36px;
    margin: 0;
    font-family: "Cormorant Garamond", Georgia, serif;
    font-weight: 500;
    font-size: 21px;
    letter-spacing: 1px;
    color: var(--name-grey);
  }
  .conditions {
    position: absolute;
    right: 548px;
    top: 103px;
    text-align: right;
    color: var(--navy);
  }
  .conditions-list {
    margin: 0;
    font-weight: 600;
    font-size: 12.5px;
    line-height: 14px;
  }
  .conditions-note, .conditions-contact {
    margin: 14px 0 0;
    font-weight: 600;
    font-size: 8.5px;
    line-height: 10px;
  }
  .conditions-contact { margin-top: 28px; }
  .weight-pitch {
    position: absolute;
    right: 45px;
    top: 138px;
    text-align: right;
    color: var(--white);
  }
  .weight-heading {
    margin: 0;
    font-weight: 400;
    font-size: 18.5px;
    line-height: 22px;
  }
  .weight-body {
    margin: 0;
    font-size: 8.2px;
    line-height: 10.4px;
  }
</style>
</head>
<body>
<div class="canvas">
  <svg class="pocket-flap" width="1200" height="916" viewBox="0 0 1200 916" aria-hidden="true">
    <path fill="var(--flap)" d="M14 653 L92 247 Q104 205 176 195 L176 710 L216 772 Q196 780 196 810 Q200 840 232 845 L270 845 L308 901 Q520 890 670 797 L670 710 L176 710 Z"/>
  </svg>

  <section class="folder-face">
    <div class="hero-photo" role="img" aria-label="Photo of a woman in a white dress with arms open in a green flowering field under a blue sky with white clouds"></div>

    <div class="conditions">
      <p class="conditions-list">Also helps with<br>Constipation -<br>Bloating -<br>IBS&nbsp; -<br>Eating disorders and overeating -</p>
      <p class="conditions-note">Our practitioner is highly experienced.<br>Please visit our web sites for reviews.</p>
      <p class="conditions-contact">Visit our web site LarkfieldTane.com<br>or<br>call 413-908-2617</p>
    </div>

    <div class="weight-pitch">
      <h1 class="weight-heading">Control your weight</h1>
      <p class="weight-body">by balancing your nervous and digestive system through<br>the Tane Method. The Tane Method, a technique developed by<br>Dr. Wenna. Tane, uses physical pressure to manipulate visceral tissue<br>to bring back resiliency and proper functioning of the whole body.</p>
    </div>

    <div class="divider-band"></div>
    <div class="anatomy-strip" role="img" aria-label="Three golden anatomical renderings of the upper back, spine and shoulders on a dark background"></div>
    <div class="name-strip" role="img" aria-label="Soft grey blurred field of white flowers">
      <p class="brand-name">Larkfield Tane Therapy</p>
    </div>
  </section>
</div>
</body>
</html>
```